Luxury Real Estate Post Card

We are a Luxury Boutique Real Estate Company located in Chicago's Gold Coast
and are looking for a Designer to design a Luxury Post Card.
We currently have one of the top ranked websites in Chicago.
Just a note, we are not big on skyline shots, would prefer to showcase one
or more of the luxury buildings listed below
* Final Proof must be print ready -
6" x 9" postcard
Vellmore Spire Chicago, Marquand, Brisk Lodgeway, Fenwold Ashby Residences etc
Tag lines: Open to suggestions
Logo - See attached
Phone Number 312-555-0147
Website: brindlehavenhomes.example
Target Market(s)
Luxury Buyers
Industry/Entity Type
Real Estate
Requirements
Must have
- Clean Design -Showcase Luxury Buildings i.e. Vellmore - Tag Lines - Front and Back

```html
<!DOCTYPE html>
<html lang="en">
<head>
<meta charset="utf-8">
<title>Brindlehaven Homes – Luxury Postcard</title>
<link rel="stylesheet" href="https://fonts.googleapis.com/css2?family=Jost:wght@300;400;500;700&family=Noto+Serif:ital@1&display=swap">
<style>
  :root {
    --stage: #000000;
    --ink: #111111;
    --gold: #a8812f;
    --paper: #ffffff;
    --muted: #8a8a8a;
    --sky-gold: #e8b93a;
    --sky-olive: #8f9a55;
    --sky-blue: #3f8fc4;
    --sky-light: #a9d3ee;
    --stone: #c9b7a8;
  }
  * { box-sizing: border-box; margin: 0; padding: 0; }
  html, body {
    width: 1200px; height: 547px; overflow: hidden;
    background: var(--stage);
    font-family: "Jost", "Futura", sans-serif;
  }
  .postcard {
    position: absolute; top: 50px;
    width: 535px; height: 357px; overflow: hidden;
  }
  .postcard--front { left: 49px; }
  .postcard--back { left: 616px; background: var(--paper); }

  .photo { position: absolute; inset: 0; }
  .photo--front {
    background:
      linear-gradient(75deg, transparent 55%, rgba(201,183,168,.55) 56%, rgba(160,140,130,.55) 75%, transparent 76%),
      linear-gradient(120deg, var(--sky-gold) 0%, #d9b55a 30%, var(--sky-olive) 55%, var(--sky-blue) 80%, #2e6f9c 100%);
  }
  .photo--back {
    right: auto; width: 336px;
    background:
      linear-gradient(100deg, rgba(190,170,150,.85) 0%, rgba(200,185,170,.85) 58%, transparent 59%),
      linear-gradient(90deg, var(--sky-blue) 0%, var(--sky-light) 60%, var(--paper) 100%);
  }

  .brand-name {
    position: absolute; font-weight: 500; color: var(--gold);
    letter-spacing: 1.5px; text-transform: uppercase; text-align: center; line-height: 1.1;
  }
  .postcard--front .brand-name { left: 19px; top: 50px; width: 112px; font-size: 15px; }
  .postcard--back .brand-name { left: 186px; top: 30px; width: 140px; font-size: 16px; }

  .contact { position: absolute; color: var(--ink); line-height: 1.2; }
  .contact__web { font-size: 9.5px; font-weight: 500; }
  .contact__phone { font-size: 16px; font-weight: 400; }
  .postcard--front .contact { right: 24px; top: 68px; text-align: right; }
  .postcard--back .contact { left: 186px; top: 95px; width: 140px; text-align: center; }

  .tagline {
    position: absolute; left: 19px; top: 252px;
    color: var(--ink); font-size: 16px; font-weight: 400; line-height: 1;
  }
  .tagline__open { display: block; font-size: 46px; font-weight: 300; line-height: 40px; letter-spacing: 1px; }
  .tagline__rest { display: block; font-size: 24px; font-weight: 400; line-height: 22px; }
  .buildings {
    position: absolute; left: 19px; top: 318px;
    font-size: 9px; font-weight: 700; line-height: 1.25; color: var(--ink);
  }

  .indicia {
    position: absolute; right: 22px; top: 14px;
    font-size: 5.5px; font-weight: 700; line-height: 1.35; text-align: right; color: var(--ink);
  }
  .return-address {
    position: absolute; left: 336px; width: 198px; top: 287px;
    font-family: "Noto Serif", serif; font-style: italic;
    font-size: 7.5px; line-height: 1.35; text-align: center; color: var(--ink);
  }
  .disclaimer {
    position: absolute; left: 336px; width: 198px; top: 320px;
    font-size: 5.5px; line-height: 1.4; text-align: center; color: var(--muted);
  }
</style>
</head>
<body>
  <section class="postcard postcard--front">
    <div class="photo photo--front" role="img" aria-label="Photo of a luxury high-rise tower seen from below against a golden and blue sky"></div>
    <div class="brand-name">Brindlehaven Homes</div>
    <div class="contact">
      <div class="contact__web">brindlehavenhomes.example</div>
      <div class="contact__phone">312-555-0147</div>
    </div>
    <h1 class="tagline">
      <span class="tagline__open">OPEN</span>
      <span class="tagline__rest">to suggestions</span>
    </h1>
    <p class="buildings">Vellmore Spire Chicago, Marquand,<br>Brisk Lodgeway, Fenwold Ashby Residences etc</p>
  </section>

  <section class="postcard postcard--back">
    <div class="photo photo--back" role="img" aria-label="Photo of a stone-clad luxury residential tower seen from below against a blue sky with clouds"></div>
    <div class="brand-name">Brindlehaven Homes</div>
    <div class="contact">
      <div class="contact__web">brindlehavenhomes.example</div>
      <div class="contact__phone">312-555-0147</div>
    </div>
    <div class="indicia">PRSRT STD<br>U.S. POSTAGE PAID<br>CHICAGO, IL<br>PERMIT NO 4471</div>
    <address class="return-address">Aldercrest Center<br>410 N. Larkspur Ave #2200<br>Chicago Il 60654</address>
    <p class="disclaimer">This publication is not intended to solicit the listing of properties<br>currently under contract with other real estate professionals.</p>
  </section>
</body>
</html>
```